I need a business Card Design for my practice , i am clinical herbalist. I am a herbalist specializing in Lyme disease, autism, autoimmune diseases, difficult to cure diseasesDifficult to cure diseases. In my innovative practice i link traditional medicine, herbs with science, immunologu ,pharmacology.

Industry/Entity Type

Business

Contact Information for Business Card

My company name : OŚRODEK ZIELNIK
My name : Tomasz Lipczak
Name of my profession : Fitoterapeuta
In Polish language Fitoterapeuta is Herbalist .

e-mail: tomaszlipczak@osrodekzielnik.com
www.osrodek-zielnik.pl
phone : 604 587 231
My company adress : Dąbrowa Sitnicka 41 , 38-415 Lużna
I dont have logo .

Requirements
Nice to have
• My company

```html
<!DOCTYPE html>
<html lang="pl">
<head>
<meta charset="utf-8">
<title>Ośrodek Zielnik – wizytówka</title>
<link rel="stylesheet" href="https://fonts.googleapis.com/css2?family=Montserrat:wght@700&family=Roboto:wght@400;500&display=swap">
<style>
  :root {
    --stage: #2f2f31;
    --plum: #6c5080;
    --paper: #ffffff;
    --leaf: #4fb648;
    --orange: #f07c1c;
    --ink: #4a4a4a;
    --ink-soft: #2e2e2e;
  }
  * { box-sizing: border-box; margin: 0; padding: 0; }
  html, body {
    width: 1200px; height: 900px; overflow: hidden;
    background: var(--stage);
  }
  .canvas { position: relative; width: 1200px; height: 900px; }
  .card {
    position: absolute; left: 280px; width: 640px; height: 366px;
    border-radius: 4px; box-shadow: 0 6px 18px rgba(0,0,0,.35);
    overflow: hidden;
  }

  /* back side */
  .card--back { top: 50px; background: var(--plum); color: var(--paper); text-align: center; }
  .back-mark {
    position: absolute; left: 0; right: 0; top: 86px;
    display: flex; flex-direction: column; align-items: center; gap: 14px;
  }
  .back-mark__dot { width: 64px; height: 64px; border-radius: 50%; background: var(--paper); }
  .back-mark__name { font: 700 36px/1 "Montserrat", sans-serif; color: var(--paper); }
  .back-tagline {
    position: absolute; left: 0; right: 0; top: 246px;
    font: 500 13px/1.6 "Roboto", sans-serif; letter-spacing: 1px; text-transform: uppercase;
  }

  /* front side */
  .card--front { top: 470px; background: var(--paper); color: var(--ink); }
  .front-title {
    position: absolute; left: 34px; top: 34px;
    font: 700 26px/1 "Montserrat", sans-serif; color: var(--ink);
  }
  .front-title__accent { color: var(--orange); }
  .person { position: absolute; left: 46px; top: 112px; }
  .person__name { font: 700 20px/1.2 "Montserrat", sans-serif; color: var(--ink-soft); }
  .person__role { font: 400 16px/1.3 "Roboto", sans-serif; color: var(--orange); margin-bottom: 6px; }
  .contact { list-style: none; font: 400 15px/1.55 "Roboto", sans-serif; color: var(--ink-soft); }
  .contact li { display: flex; align-items: center; gap: 8px; white-space: nowrap; }
  .contact .icon { width: 14px; height: 14px; flex: none; }
  .contact .no-icon { width: 14px; flex: none; }
  .front-mark {
    position: absolute; right: 44px; top: 90px; width: 230px;
    display: flex; flex-direction: column; align-items: center; gap: 18px;
  }
  .front-mark__dot { width: 130px; height: 130px; border-radius: 50%; background: var(--leaf); }
  .front-mark__name { font: 700 22px/1 "Montserrat", sans-serif; color: var(--plum); white-space: nowrap; }
</style>
</head>
<body>
<main class="canvas">

  <section class="card card--back" aria-label="Rewers wizytówki">
    <div class="back-mark">
      <span class="back-mark__dot"></span>
      <span class="back-mark__name">Ośrodek Zielnik</span>
    </div>
    <p class="back-tagline">Specializing in<br>Lyme disease | Autism | Autoimmune diseases</p>
  </section>

  <section class="card card--front" aria-label="Awers wizytówki">
    <h1 class="front-title">Ośrodek <span class="front-title__accent">Zielnik</span></h1>

    <div class="person">
      <p class="person__name">Tomasz Lipczak</p>
      <p class="person__role">Fitoterapeuta</p>
      <ul class="contact">
        <li><span class="no-icon"></span>Dąbrowa Sitnicka 41, 38-415 Zarzecze Małe</li>
        <li>
          <svg class="icon" viewBox="0 0 24 24" aria-hidden="true"><path fill="#4fb648" d="M6.6 10.8a15.1 15.1 0 0 0 6.6 6.6l2.2-2.2c.3-.3.7-.4 1-.2 1.1.4 2.3.6 3.6.6.6 0 1 .4 1 1V20c0 .6-.4 1-1 1A17 17 0 0 1 3 4c0-.6.4-1 1-1h3.5c.6 0 1 .4 1 1 0 1.3.2 2.5.6 3.6.1.3 0 .7-.2 1z"/></svg>
          604-587-231
        </li>
        <li>
          <svg class="icon" viewBox="0 0 24 24" aria-hidden="true"><rect x="2" y="5" width="20" height="14" rx="1" fill="#4fb648"/><path d="M2.5 6l9.5 7 9.5-7" fill="none" stroke="#fff" stroke-width="1.6"/></svg>
          tomaszlipczak@osrodekzielnik.com
        </li>
        <li>
          <svg class="icon" viewBox="0 0 24 24" aria-hidden="true"><g fill="none" stroke="#4fb648" stroke-width="2"><circle cx="12" cy="12" r="9.5"/><ellipse cx="12" cy="12" rx="4" ry="9.5"/><path d="M2.5 12h19M4 7h16M4 17h16"/></g></svg>
          www.osrodek-zielnik.pl
        </li>
      </ul>
    </div>

    <div class="front-mark">
      <span class="front-mark__dot"></span>
      <span class="front-mark__name">Ośrodek Zielnik</span>
    </div>
  </section>

</main>
</body>
</html>
```